Adorable Luxury Flower Shop

Need a beautiful, eye catching, elegant full-service website.
INSPIRATIONS ARE;
https://www.quillmoreblooms.com

Industry/Entity Type

retail, floral, boutique

Coding

Coded - Design and coding required

Number of Pages Required

3 page

Requirements
Must have
• SEO, Coded, UX, Fully responsive mobile, tablet, desktop, Ecommerce setup with Square, payments integration (if we use squarespace). SEO optimization with keywords, tags, meta descriptions, Load speed optimization, Google my business setup.
Nice to have
• pictures, color, elegance

```html
<!DOCTYPE html>
<html lang="en">
<head>
<meta charset="UTF-8">
<title>Rosavelle Flower Boutique</title>
<link href="https://fonts.googleapis.com/css2?family=Lora:ital,wght@0,400;0,500;0,600;0,700;1,400&family=Lato:wght@400;700&display=swap" rel="stylesheet">
<style>
:root{
  --red:#b3141c;
  --red-dark:#9c0f16;
  --ink:#222;
  --muted:#666;
  --soft:#ececec;
  --black:#0d0d0d;
  --white:#fff;
  --gold:#f2a223;
}
*{margin:0;padding:0;box-sizing:border-box}
html,body{width:1200px;height:4545px;overflow:hidden;background:var(--white)}
body{font-family:"Lora",serif;color:var(--ink)}
.page{position:relative;width:1200px;height:4545px;overflow:hidden}
.abs{position:absolute}
/* top bar */
.topbar{top:0;left:0;width:1200px;height:39px;background:var(--red);color:#fff;font-family:"Lato",sans-serif;font-size:13px}
.topbar .call{left:113px;top:11px}
.topbar .promo{left:0;width:1200px;text-align:center;top:11px;font-family:"Lora",serif}
.topbar .promo u{color:#ffc9c9}
.topbar .socials{right:116px;top:12px;display:flex;gap:10px}
.topbar .socials span{width:14px;height:14px;border:1.5px solid #fff;border-radius:50%}
/* header */
.header{top:39px;left:0;width:1200px;height:93px;background:#fff;z-index:3}
.brand{left:111px;top:8px;width:190px;height:130px;border-radius:50%;background:#fff;display:flex;align-items:center;justify-content:center;flex-direction:column;box-shadow:0 2px 6px rgba(0,0,0,.08)}
.brand .name{font-family:"Lora",serif;font-weight:700;font-size:27px;color:var(--ink);letter-spacing:.5px}
.brand .sub{font-size:8px;color:var(--ink);letter-spacing:2px;margin-top:2px}
.nav{top:41px;left:0;width:1200px;font-size:12px;font-family:"Lora",serif}
.nav a{position:absolute;color:var(--ink);text-decoration:none;transform:translateX(-50%);white-space:nowrap}
.nav a.active{color:var(--red)}
.nav .dot{position:absolute;left:446px;top:20px;width:9px;height:9px;border-radius:50%;background:var(--red);transform:translateX(-50%)}
.header svg{position:absolute;top:38px}
/* hero */
.hero{top:132px;left:0;width:1200px;height:660px;background:radial-gradient(circle at 85% 25%,#f1e6c8 0,#e0b98a 12%,transparent 28%),radial-gradient(circle at 60% 45%,#e3873c 0,#c4632a 20%,transparent 42%),radial-gradient(circle at 30% 70%,#d27a3a 0,transparent 35%),linear-gradient(120deg,#3f4a2a 0%,#6b5a32 35%,#a8582a 60%,#5c4a2a 100%)}
.hero-shade{top:132px;left:0;width:1200px;height:660px;background:linear-gradient(90deg,rgba(0,0,0,.35),rgba(0,0,0,0) 70%)}
.hero-title{left:113px;top:312px;color:#fff;font-weight:500;font-size:37px;line-height:56px;text-transform:uppercase;white-space:nowrap}
.hero-text{left:113px;top:428px;width:640px;color:#fff;font-style:italic;font-size:14px;line-height:23px}
.btn{display:inline-flex;align-items:center;justify-content:center;background:var(--red);color:#fff;border-radius:30px;font-size:14px;text-transform:uppercase;font-family:"Lora",serif}
.hero-btn{left:113px;top:496px;width:146px;height:48px;font-size:15px}
.hero-dots{top:732px;left:576px;display:flex;gap:6px}
.hero-dots span{width:11px;height:11px;border-radius:50%;border:2px solid #fff}
.hero-dots span.on{background:var(--red);border-color:var(--red)}
/* section titles */
.sec-title{left:0;width:1200px;text-align:center;font-size:31px;text-transform:uppercase;font-weight:400}
.sec-title span{display:inline-block;position:relative;padding:6px 8px;border-top:1px solid #999;border-bottom:1px solid #999}
.sec-title span::before,.sec-title span::after{content:"";position:absolute;top:50%;width:18px;height:18px;border-radius:50%;background:var(--red);transform:translateY(-50%)}
.sec-title span::before{left:-26px}
.sec-title span::after{right:-26px}
.sec-title.light{color:#fff}
.sec-title.light span{border-color:rgba(255,255,255,.7)}
.sec-title.light span::before,.sec-title.light span::after{background:#7a0b10}
/* products */
.product{width:233px}
.product .ph{width:233px;height:312px}
.product .pname{margin-top:14px;font-size:19px}
.product .price{margin-top:4px;font-size:19px;color:var(--red);font-weight:500}
/* holiday */
.holiday-bg{top:1760px;left:0;width:1200px;height:520px;background:linear-gradient(180deg,#f3f3f3,#e4e4e4)}
.holiday-text{left:150px;top:1960px;width:475px;text-align:center;font-style:italic;font-size:12px;line-height:19px}
.countdown{top:2020px;left:160px;display:flex;gap:22px;align-items:flex-start}
.countdown .unit{width:78px;text-align:center}
.countdown .num{font-size:42px;line-height:52px}
.countdown .lbl{font-size:12px;color:var(--muted);font-family:"Lato",sans-serif}
.countdown .colon{font-size:36px;line-height:62px}
.holiday-btn{left:330px;top:2125px;width:134px;height:37px;font-size:13px}
.holiday-img{left:644px;top:1835px;width:530px;height:424px;border-radius:8px;background:radial-gradient(circle at 40% 30%,#d9a6d3,#bf7db8 25%,transparent 45%),radial-gradient(circle at 65% 70%,#f4c3cf,#eaa3b5 30%,transparent 55%),linear-gradient(160deg,#f0eef0,#e2dde0)}
/* occasions */
.occ-bg{top:2224px;left:0;width:1200px;height:512px;background:radial-gradient(circle at 30% 50%,#c21a22,#a7121a 70%)}
.occ{width:200px;text-align:center;color:#fff;text-transform:uppercase;font-size:17px}
.occ .ring{width:109px;height:109px;margin:0 auto 18px;border:3px solid #fff;border-radius:50%;display:flex;align-items:center;justify-content:center}
.arrow{width:30px;height:30px;border-radius:50%;display:flex;align-items:center;justify-content:center}
.arrow.onred{border:1.5px solid #fff}
.arrow.ongray{border:1.5px solid #999}
/* testimonials */
.card{top:2891px;width:307px;height:277px;border:1px solid #ddd;box-shadow:0 2px 6px rgba(0,0,0,.12);background:#fff;padding:22px 20px}
.card .stars{color:var(--gold);font-size:14px;letter-spacing:1px}
.card .who{font-family:"Lato",sans-serif;font-size:15px;margin-top:8px;text-transform:uppercase}
.card .quote{position:absolute;right:18px;top:-10px;font-size:130px;color:#e3e3e3;line-height:1}
.card p{margin-top:24px;font-style:italic;font-size:12px;line-height:21px;color:var(--muted);padding:0 6px}
.reviews-btn{left:507px;top:3198px;width:187px;height:46px;font-size:13px}
/* top sell */
.sell-bg{top:3330px;left:0;width:1200px;height:470px;background:linear-gradient(180deg,#eeeeee,#e2e2e2)}
.sell{top:3459px;width:229px;height:295px;background:#fff;border:1px solid #ddd;padding:4px}
.sell .ph{height:208px;position:relative}
.sell .tag{position:absolute;left:8px;top:12px;background:var(--red);color:#fff;font-size:11px;padding:3px 10px;border-radius:12px}
.sell .ico{position:absolute;right:10px;width:22px;height:22px;border-radius:50%;background:#fff;border:1px solid #bbb;display:flex;align-items:center;justify-content:center}
.sell .pname{margin:18px 0 0 6px;font-size:16px}
.sell .price{margin:8px 0 0 6px;font-size:14px}
.sell .price s{color:#999;margin-left:10px}
/* newsletter */
.news-bg{top:3777px;left:0;width:1200px;height:420px;background:radial-gradient(circle at 50% 60%,#c41a22,#a5111a 75%)}
.news-text{left:250px;top:3995px;width:700px;text-align:center;color:#fff;font-style:italic;font-size:13px;line-height:27px}
.news-form{left:258px;top:4072px;width:683px;height:44px;background:#fff;border-radius:24px}
.news-form .ph-text{position:absolute;left:20px;top:14px;font-size:12px;font-style:italic;color:#555}
.news-form .sub{position:absolute;right:0;top:0;width:159px;height:44px;border-radius:24px;background:var(--black);color:#fff;font-size:13px;display:flex;align-items:center;justify-content:center}
/* footer */
.footer-bg{top:4183px;left:0;width:1200px;height:362px;background:var(--black)}
.foot-brand{left:120px;top:4236px;width:254px;height:176px;border-radius:50%;border:2px solid #fff;display:flex;flex-direction:column;align-items:center;justify-content:center;color:#fff}
.foot-brand .name{font-size:36px;font-weight:700}
.foot-brand .sub{font-size:9px;letter-spacing:3px}
.foot h4{color:#fff;font-size:19px;font-weight:600;text-transform:uppercase;letter-spacing:.5px}
.contact{display:flex;gap:14px;margin-top:22px;color:#fff;font-family:"Lato",sans-serif;font-size:12px;line-height:18px}
.contact .ic{width:40px;height:40px;border:1.5px solid #fff;border-radius:50%;display:flex;align-items:center;justify-content:center;flex:none}
.links{list-style:none;color:#fff;font-family:"Lato",sans-serif;font-size:13px}
.links li{height:30px;display:flex;align-items:center}
.links li::before{content:"›";margin-right:22px;font-size:16px}
.fsoc{top:4389px;left:877px;display:flex;gap:9px}
.fsoc span{width:40px;height:40px;border-radius:50%;border:2px solid #fff}
.fsoc span.on{background:var(--red)}
.divider{top:4492px;left:111px;width:978px;height:1px;background:#333}
.copy{top:4505px;left:0;width:1200px;text-align:center;color:#ddd;font-family:"Lato",sans-serif;font-size:13px}
</style>
</head>
<body>
<div class="page">

<div class="abs topbar">
  <div class="abs call">Call Us : 000-000-00000</div>
  <div class="abs promo">Sign up and GET30% OFF for your first order <u>Sign up now</u></div>
  <div class="abs socials"><span></span><span></span><span></span></div>
</div>

<div class="abs hero" role="img" aria-label="Close-up photograph of orange and cream roses"></div>
<div class="abs hero-shade"></div>
<svg class="abs" style="top:560px;left:0" width="1200" height="240" viewBox="0 0 1200 240">
  <path d="M0 68 C250 210 520 220 700 205 C900 185 1080 110 1200 20 L1200 240 L0 240 Z" fill="#fff"/>
  <path d="M250 182 C450 225 650 222 800 200 C980 172 1100 110 1200 25" fill="none" stroke="#b3141c" stroke-width="5"/>
</svg>
<h1 class="abs hero-title">Welcome to<br>Rosavelle Flower Boutique</h1>
<p class="abs hero-text">The point of using Lorem Ipsum is that it has a more-or-less normal distribution of letters, as opposed to using 'Content here, content here', making it look like readable English.</p>
<div class="abs btn hero-btn">Shop Now</div>
<div class="abs hero-dots"><span class="on"></span><span></span><span></span></div>

<div class="abs header">
  <div class="abs brand"><div class="name">ROSAVELLE</div><div class="sub">FLOWER BOUTIQUE</div></div>
  <div class="abs nav">
    <a class="active" style="left:446px">HOME</a>
    <a style="left:522px">ABOUT US</a>
    <a style="left:614px">PRODUCTS</a>
    <a style="left:709px">OCCASIONS</a>
    <a style="left:819px">TESTIMONIALS</a>
    <a style="left:934px">CONTACT US</a>
    <span class="dot"></span>
  </div>
  <svg style="left:987px" width="18" height="18" viewBox="0 0 18 18"><circle cx="7.5" cy="7.5" r="5.5" fill="none" stroke="#333" stroke-width="1.6"/><path d="M11.5 11.5 L16 16" stroke="#333" stroke-width="1.6"/></svg>
  <svg style="left:1028px" width="18" height="18" viewBox="0 0 18 18"><circle cx="9" cy="6" r="4" fill="none" stroke="#333" stroke-width="1.5"/><path d="M2 17 C3 11 15 11 16 17" fill="none" stroke="#333" stroke-width="1.5"/></svg>
  <svg style="left:1070px" width="18" height="18" viewBox="0 0 18 18"><path d="M3 5 H15 L14 16 H4 Z" fill="none" stroke="#333" stroke-width="1.5"/><path d="M6 7 V4 a3 3 0 0 1 6 0 V7" fill="none" stroke="#333" stroke-width="1.5"/></svg>
</div>

<h2 class="abs sec-title" style="top:828px"><span>Featured Products</span></h2>

<div class="abs product" style="left:111px;top:918px"><div class="ph" role="img" aria-label="Bouquet of dahlias and mixed blooms held in hand" style="background:radial-gradient(circle at 50% 40%,#c05a3a,#a87aa0 35%,#8e8e8e 75%)"></div><div class="pname">Product Name</div><div class="price">$25.00</div></div>
<div class="abs product" style="left:360px;top:918px"><div class="ph" role="img" aria-label="Autumn arrangement with sunflowers in a wooden pot" style="background:radial-gradient(circle at 50% 45%,#e49a2a,#b85a22 40%,#6b5340 80%)"></div><div class="pname">Product Name</div><div class="price">$25.00</div></div>
<div class="abs product" style="left:607px;top:918px"><div class="ph" role="img" aria-label="Hands arranging a protea bouquet" style="background:radial-gradient(circle at 50% 35%,#e7b4b8,#5d7a55 45%,#3a4a3a 85%)"></div><div class="pname">Product Name</div><div class="price">$25.00</div></div>
<div class="abs product" style="left:856px;top:918px"><div class="ph" role="img" aria-label="Neutral toned bouquet in a glass vase" style="background:radial-gradient(circle at 50% 40%,#d8c2a8,#8f8a80 45%,#5e5a55 85%)"></div><div class="pname">Product Name</div><div class="price">$25.00</div></div>

<div class="abs product" style="left:111px;top:1324px"><div class="ph" role="img" aria-label="Peach bouquet standing on a table" style="background:radial-gradient(circle at 50% 30%,#e5a58a,#4b5a48 45%,#2e302c 85%)"></div><div class="pname">Product Name</div><div class="price">$25.00</div></div>
<div class="abs product" style="left:360px;top:1324px"><div class="ph" role="img" aria-label="Red and pink bouquet wrapped in kraft paper" style="background:radial-gradient(circle at 50% 45%,#d84a4a,#e7a4a0 35%,#c9a57c 75%)"></div><div class="pname">Product Name</div><div class="price">$25.00</div></div>
<div class="abs product" style="left:607px;top:1324px"><div class="ph" role="img" aria-label="Pink hatbox filled with roses" style="background:radial-gradient(circle at 50% 40%,#c23a7a,#e57aa8 40%,#3f5a3a 85%)"></div><div class="pname">Product Name</div><div class="price">$25.00</div></div>
<div class="abs product" style="left:856px;top:1324px"><div class="ph" role="img" aria-label="Coral roses in terracotta pots" style="background:radial-gradient(circle at 50% 40%,#ef9a88,#c76f5a 40%,#4a3a30 85%)"></div><div class="pname">Product Name</div><div class="price">$25.00</div></div>

<div class="abs holiday-bg"></div>
<svg class="abs" style="top:1740px;left:0" width="1200" height="70" viewBox="0 0 1200 70">
  <path d="M0 70 L0 62 C300 10 900 0 1200 38 L1200 70 Z" fill="#b3141c"/>
  <path d="M0 70 C300 22 900 14 1200 48 L1200 70 Z" fill="#f3f3f3"/>
</svg>
<div class="abs holiday-img" role="img" aria-label="Pink and lilac rose arrangement in a pastel gift box"></div>
<h2 class="abs sec-title" style="top:1886px;left:150px;width:475px"><span>Holiday Sales</span></h2>
<p class="abs holiday-text">It is a long established fact that a reader will be distracted by the readable content of a page when looking at its layout.</p>
<div class="abs countdown">
  <div class="unit"><div class="num">05</div><div class="lbl">Days</div></div><div class="colon">:</div>
  <div class="unit"><div class="num">15</div><div class="lbl">Hours</div></div><div class="colon">:</div>
  <div class="unit"><div class="num">55</div><div class="lbl">Minutes</div></div><div class="colon">:</div>
  <div class="unit"><div class="num">45</div><div class="lbl">Secounds</div></div>
</div>
<div class="abs btn holiday-btn">Shop Now</div>

<div class="abs occ-bg" role="img" aria-label="Red background with faint rose texture"></div>
<svg class="abs" style="top:2200px;left:0" width="1200" height="80" viewBox="0 0 1200 80">
  <path d="M0 0 L1200 0 L1200 30 C900 75 300 75 0 30 Z" fill="#e4e4e4"/>
</svg>
<h2 class="abs sec-title light" style="top:2341px"><span>Shop by Occasions</span></h2>
<div class="abs occ" style="left:85px;top:2449px"><div class="ring"><svg width="50" height="50" viewBox="0 0 50 50"><circle cx="25" cy="30" r="13" fill="none" stroke="#fff" stroke-width="3"/><path d="M19 16 L25 8 L31 16 Z" fill="none" stroke="#fff" stroke-width="2.5"/></svg></div>Weddings</div>
<div class="abs occ" style="left:264px;top:2525px"><div class="ring"><svg width="50" height="50" viewBox="0 0 50 50"><rect x="10" y="22" width="30" height="18" fill="none" stroke="#fff" stroke-width="2.5"/><path d="M17 22 V14 M25 22 V12 M33 22 V14" stroke="#fff" stroke-width="2.5"/></svg></div>Birthday</div>
<div class="abs occ" style="left:481px;top:2449px"><div class="ring"><svg width="50" height="50" viewBox="0 0 50 50"><path d="M12 40 L22 12 L38 28 Z" fill="none" stroke="#fff" stroke-width="2.5"/><path d="M32 10 L36 6 M38 16 L44 14" stroke="#fff" stroke-width="2.5"/></svg></div>Congratulations</div>
<div class="abs occ" style="left:708px;top:2525px"><div class="ring"><svg width="50" height="50" viewBox="0 0 50 50"><path d="M25 40 L10 25 a8 8 0 0 1 15 -10 a8 8 0 0 1 15 10 Z" fill="none" stroke="#fff" stroke-width="2.5"/></svg></div>Anniversary</div>
<div class="abs occ" style="left:899px;top:2448px"><div class="ring"><svg width="50" height="50" viewBox="0 0 50 50"><path d="M25 40 L10 25 a8 8 0 0 1 15 -10 a8 8 0 0 1 15 10 Z" fill="none" stroke="#fff" stroke-width="2.5"/><path d="M16 26 L22 32 L34 22" fill="none" stroke="#fff" stroke-width="2.5"/></svg></div>Thank You</div>
<div class="abs arrow onred" style="left:1134px;top:2488px"><svg width="12" height="12" viewBox="0 0 12 12"><path d="M4 2 L8 6 L4 10" fill="none" stroke="#fff" stroke-width="2"/></svg></div>
<div class="abs arrow onred" style="left:1134px;top:2526px"><svg width="12" height="12" viewBox="0 0 12 12"><path d="M8 2 L4 6 L8 10" fill="none" stroke="#fff" stroke-width="2"/></svg></div>

<h2 class="abs sec-title" style="top:2791px"><span>What Our Clients Saying</span></h2>
<div class="abs card" style="left:111px"><div class="quote">”</div><div class="stars">★★★★☆</div><div class="who">Mara Lind</div><p>It is a long established fact that a reader will be distracted by the readable content of page when looking at its layout. The point of using Lorem Ipsum is that it has a more-or-less normal distribution of letters the point of using Lorem Ipsum is that it has a more less normal distribution of letters</p></div>
<div class="abs card" style="left:448px"><div class="quote">”</div><div class="stars">★★★★☆</div><div class="who">Mara Lind</div><p>It is a long established fact that a reader will be distracted by the readable content of page when looking at its layout. The point of using Lorem Ipsum is that it has a more-or-less normal distribution of letters the point of using Lorem Ipsum is that it has a more less normal distribution of letters</p></div>
<div class="abs card" style="left:784px"><div class="quote">”</div><div class="stars">★★★★☆</div><div class="who">Mara Lind</div><p>It is a long established fact that a reader will be distracted by the readable content of page when looking at its layout. The point of using Lorem Ipsum is that it has a more-or-less normal distribution of letters the point of using Lorem Ipsum is that it has a more less normal distribution of letters</p></div>
<div class="abs btn reviews-btn">View More Reviews</div>

<div class="abs sell-bg"></div>
<svg class="abs" style="top:3296px;left:0" width="1200" height="70" viewBox="0 0 1200 70">
  <path d="M0 70 L0 58 C300 8 900 0 1200 38 L1200 70 Z" fill="#b3141c"/>
  <path d="M0 70 C300 20 900 14 1200 48 L1200 70 Z" fill="#eeeeee"/>
</svg>
<h2 class="abs sec-title" style="top:3365px"><span>Our Top Sell Products</span></h2>

<div class="abs sell" style="left:111px"><div class="ph" role="img" aria-label="Mixed purple and yellow bouquet" style="background:radial-gradient(circle at 50% 40%,#a06ab0,#d9c24a 35%,#e8e8e8 70%)"><span class="tag">25% OFF</span><span class="ico" style="top:148px"><svg width="11" height="11" viewBox="0 0 12 12"><path d="M6 10 L1.5 5.5 a2.5 2.5 0 0 1 4.5 -3 a2.5 2.5 0 0 1 4.5 3 Z" fill="none" stroke="#555" stroke-width="1.2"/></svg></span><span class="ico" style="top:178px"><svg width="11" height="11" viewBox="0 0 12 12"><path d="M2 4 H10 L9.5 11 H2.5 Z" fill="none" stroke="#555" stroke-width="1.2"/></svg></span></div><div class="pname">Product Name</div><div class="price">$55.00 <s>$75.00</s></div></div>
<div class="abs sell" style="left:362px"><div class="ph" role="img" aria-label="Bright tulip bouquet on pink" style="background:radial-gradient(circle at 50% 40%,#e8467a,#f4a0b8 40%,#f7d7e0 75%)"><span class="tag">25% OFF</span><span class="ico" style="top:148px"><svg width="11" height="11" viewBox="0 0 12 12"><path d="M6 10 L1.5 5.5 a2.5 2.5 0 0 1 4.5 -3 a2.5 2.5 0 0 1 4.5 3 Z" fill="none" stroke="#555" stroke-width="1.2"/></svg></span><span class="ico" style="top:178px"><svg width="11" height="11" viewBox="0 0 12 12"><path d="M2 4 H10 L9.5 11 H2.5 Z" fill="none" stroke="#555" stroke-width="1.2"/></svg></span></div><div class="pname">Product Name</div><div class="price">$55.00 <s>$75.00</s></div></div>
<div class="abs sell" style="left:611px"><div class="ph" role="img" aria-label="White rose bouquet" style="background:radial-gradient(circle at 50% 40%,#f6f3ea,#d8d6c8 40%,#7d8b70 75%,#f2f2f2 95%)"><span class="tag">25% OFF</span><span class="ico" style="top:148px"><svg width="11" height="11" viewBox="0 0 12 12"><path d="M6 10 L1.5 5.5 a2.5 2.5 0 0 1 4.5 -3 a2.5 2.5 0 0 1 4.5 3 Z" fill="none" stroke="#555" stroke-width="1.2"/></svg></span><span class="ico" style="top:178px"><svg width="11" height="11" viewBox="0 0 12 12"><path d="M2 4 H10 L9.5 11 H2.5 Z" fill="none" stroke="#555" stroke-width="1.2"/></svg></span></div><div class="pname">Product Name</div><div class="price">$55.00 <s>$75.00</s></div></div>
<div class="abs sell" style="left:860px"><div class="ph" role="img" aria-label="Pink and red bouquet with ribbon" style="background:radial-gradient(circle at 50% 40%,#e36a6a,#f3b2b8 40%,#f2f0f0 75%)"><span class="tag">25% OFF</span><span class="ico" style="top:148px"><svg width="11" height="11" viewBox="0 0 12 12"><path d="M6 10 L1.5 5.5 a2.5 2.5 0 0 1 4.5 -3 a2.5 2.5 0 0 1 4.5 3 Z" fill="none" stroke="#555" stroke-width="1.2"/></svg></span><span class="ico" style="top:178px"><svg width="11" height="11" viewBox="0 0 12 12"><path d="M2 4 H10 L9.5 11 H2.5 Z" fill="none" stroke="#555" stroke-width="1.2"/></svg></span></div><div class="pname">Product Name</div><div class="price">$55.00 <s>$75.00</s></div></div>
<div class="abs arrow ongray" style="left:1134px;top:3545px"><svg width="12" height="12" viewBox="0 0 12 12"><path d="M4 2 L8 6 L4 10" fill="none" stroke="#888" stroke-width="2"/></svg></div>
<div class="abs arrow ongray" style="left:1134px;top:3584px"><svg width="12" height="12" viewBox="0 0 12 12"><path d="M8 2 L4 6 L8 10" fill="none" stroke="#888" stroke-width="2"/></svg></div>

<div class="abs news-bg" role="img" aria-label="Red background with faint rose texture"></div>
<svg class="abs" style="top:3760px;left:0" width="1200" height="80" viewBox="0 0 1200 80">
  <path d="M0 0 L1200 0 L1200 30 C900 78 300 78 0 30 Z" fill="#e2e2e2"/>
</svg>
<h2 class="abs sec-title light" style="top:3924px"><span>Our Newsletter Signup</span></h2>
<p class="abs news-text">Lorem ipsum dolor sit amet, consectetur adipiscing elit, sed do eiusmod tempor incididunt ut labore et enim ad minim veniam, quis nostrud exercitation ullamco</p>
<div class="abs news-form"><span class="ph-text">Enter Email Address :</span><span class="sub">SUBSCRIBE</span></div>

<div class="abs footer-bg"></div>
<svg class="abs" style="top:4170px;left:0" width="1200" height="50" viewBox="0 0 1200 50">
  <path d="M0 0 L1200 0 L1200 20 C900 48 300 48 0 20 Z" fill="#a5111a"/>
</svg>
<div class="abs foot-brand"><div class="name">ROSAVELLE</div><div class="sub">FLOWER BOUTIQUE</div></div>

<div class="abs foot" style="left:402px;top:4226px;width:230px">
  <h4>Address</h4>
  <div class="contact"><span class="ic"><svg width="16" height="16" viewBox="0 0 16 16"><path d="M3 1.5 L6 1.5 L7 5 L5 6.5 C6 9 7 10 9.5 11 L11 9 L14.5 10 L14.5 13 C8 14 2 8 3 1.5 Z" fill="none" stroke="#fff" stroke-width="1.3"/></svg></span><div>PHONE NUMBER<br>000.000.0000</div></div>
  <div class="contact"><span class="ic"><svg width="16" height="16" viewBox="0 0 16 16"><rect x="2" y="4" width="12" height="9" fill="none" stroke="#fff" stroke-width="1.3"/><path d="M2 4 L8 9 L14 4" fill="none" stroke="#fff" stroke-width="1.3"/></svg></span><div>EMAIL US<br>info@rosavelle.com</div></div>
  <div class="contact"><span class="ic"><svg width="16" height="16" viewBox="0 0 16 16"><path d="M8 15 C4 10 3 8 3 6 a5 5 0 0 1 10 0 C13 8 12 10 8 15 Z" fill="none" stroke="#fff" stroke-width="1.3"/><circle cx="8" cy="6" r="1.8" fill="#fff"/></svg></span><div>ADDRESS<br>2236 72nd Lorem ipsum<br>Duumy lorem</div></div>
</div>

<div class="abs foot" style="left:665px;top:4226px">
  <h4>Quick Links</h4>
  <ul class="links" style="margin-top:16px">
    <li>Home</li><li>About Us</li><li>Products</li><li>Occasions</li><li>Testimonials</li><li>Gallery</li><li>Contact Us</li>
  </ul>
</div>

<div class="abs foot" style="left:874px;top:4226px">
  <h4>Store Hours</h4>
  <ul class="links" style="margin-top:16px">
    <li>Monday - Friday 9am - 4pm</li><li>Saturday - 10am - 4pm</li><li>Sunday - 11am - 4pm</li>
  </ul>
</div>
<div class="abs fsoc"><span></span><span class="on"></span><span></span></div>

<div class="abs divider"></div>
<div class="abs copy">©2025 Rosavelle. All rights reserved.</div>

</div>
</body>
</html>
```